NOTE: I PROVIDED THE INCORRECT LOGO AND ONLY A HANDFUL OF PEOPLE NOTICED THAT IT WAS NOT THE ONE I DESCRIBED. THE LOGO I HAVE NOW ATTACHED MATCHES MY WEBSITE AND THE COLORS ON THE WEBSITE SHOULD BE USED FOR THE CARD.

PLEASE READ THE BUSINESS CARD DETAILS AND PROJECT MUST HAVES CAREFULLY.

I am looking for a business card that is powerful, a bit edgy, and although I work in the corporate world, not too formal. I would like to see designs that use the colors on my website www.brightlumo.com. I don't want the card to look washed out so please use shades of those colors that make them "pop". The "vibe" of the card needs to show substance and confidence while also reflecting that we're not your usual consultants.

The focus of my work is turning "people problems" into profits. Those problems could be poor service, an unstable workforce, untrained leaders, or managing change. We are an aggressive, results-focused team of performance improvement professionals who refuse to believe "things can't be done". For us, failure is not an option. Our logo reflects a target from the view of the site on a gun.

In addition to the contact information provided on the sample business card (do not include "turning people problems into profits"), I would like to include this statement (probably on the back):
I equip results-oriented business leaders to turn their people problems into profits in six months or less.

PLEASE NOTE THAT MY WEBSITE IS UNDER REVISION TO TONE DOWN THE MILITARY THEME, ALTHOUGH THE WARRIOR ENERGY AND FOCUS ON RESULTS REMAINS.

Target Market(s)

My clients are Mid and senior-level managers. I don't target any particular industry.

Industry/Entity Type

Consulting

Contact Information for Business Card

In addition to the contact information provided on the sample business card (DO NOT INCLUDE "turning people problems into profits"), I would like to include this statement (probably on the back):

I don't care whether the card is landscape or portrait view.

Font styles to use
Sans Serif

Requirements
Must have
• 1. be easy to read, no 6-8 point fonts!
• 2. a "vibe" that captures the eye without being too chaotic or busy
• 3. bold color, not washed out or boring - a good blend with the colors currently on my website (black, red, white, army green) but you don't need to use all of them.
• 4. all the contact information I have provided
• 5. a good blend with the colors currently on my website
• 6. Must have this quote on the back of the card: I equip results-oriented business leaders to turn their people problems into profits in six months or less.
Nice to have
• In looking at the sample images I provided for ideas, you can see that I like the way a card carries over from one side to the next.
• It would be great to find some aspect/quality/feature that I haven't seen before
Should not have
• 1. NO use of ALL CAPS
• 2. fonts that I would have to seek out and purchase (you should provide files for font if using something not standard)

```html
<!DOCTYPE html>
<html lang="en">
<head>
<meta charset="utf-8">
<title>Brightlumo Partners business card</title>
<link rel="stylesheet" href="https://fonts.googleapis.com/css2?family=Fira+Sans:ital,wght@0,400;1,600&family=Questrial&display=swap">
<style>
  :root {
    --backdrop: #1c1c1c;
    --card-white: #ffffff;
    --army-green: #3f4230;
    --ink: #3a3a3a;
    --rule: #b8b8a8;
    --target-red: #e0161e;
    --fire-deep: #8a3a0c;
    --fire-mid: #d97a1c;
    --fire-bright: #f6d27a;
    --quote-ink: #0a0a0a;
  }
  * { margin: 0; padding: 0; box-sizing: border-box; }
  html, body { width: 1200px; height: 1200px; overflow: hidden; }
  body {
    background: var(--backdrop);
    position: relative;
    font-family: "Fira Sans", sans-serif;
  }
  .card { position: absolute; overflow: hidden; }

  .card-front {
    left: 175px; top: 165px; width: 755px; height: 430px;
    background: var(--card-white);
    color: var(--ink);
  }
  .person-name {
    position: absolute; left: 39px; top: 42px;
    font-family: "Questrial", sans-serif;
    font-size: 48px; font-weight: 400; color: var(--army-green);
    line-height: 1; letter-spacing: 0.2px;
  }
  .person-title {
    position: absolute; left: 40px; top: 95px;
    font-size: 19px; color: #505050; line-height: 1;
  }
  .divider {
    position: absolute; left: 39px; top: 147px; width: 395px; height: 1px;
    background: linear-gradient(to right, var(--rule), rgba(184,184,168,0));
  }
  .company-name {
    position: absolute; left: 37px; top: 174px;
    font-size: 28px; color: var(--army-green); line-height: 1; font-weight: 400;
  }
  .address {
    position: absolute; left: 41px; top: 220px;
    font-size: 19px; line-height: 32px; color: #4a4a4a;
  }
  .contact-list {
    position: absolute; left: 36px; top: 298px; list-style: none;
    font-size: 19px; color: #4a4a4a;
  }
  .contact-list li { display: flex; align-items: center; height: 26.5px; }
  .contact-list svg { width: 20px; height: 18px; margin-right: 10px; flex: none; }

  .brand-mark {
    position: absolute; left: 520px; top: 120px; width: 220px;
    display: flex; flex-direction: column; align-items: center; gap: 16px;
  }
  .brand-dot {
    width: 110px; height: 110px; border-radius: 50%;
    background: var(--army-green);
  }
  .brand-name {
    font-size: 34px; font-weight: 400; color: var(--army-green); line-height: 1;
  }

  .card-back {
    left: 293px; top: 649px; width: 713px; height: 406px;
  }
  .fire-field {
    position: absolute; inset: 0;
    background:
      radial-gradient(ellipse at 85% 45%, var(--fire-bright) 0%, rgba(246,210,122,0) 45%),
      radial-gradient(ellipse at 15% 85%, #f3c060 0%, rgba(243,192,96,0) 40%),
      radial-gradient(ellipse at 55% 20%, var(--fire-deep) 0%, rgba(138,58,12,0) 50%),
      linear-gradient(135deg, var(--fire-mid), #c4601a 50%, var(--fire-mid));
  }
  .mission {
    position: absolute; left: 371px; top: 238px; width: 335px;
    font-size: 27px; font-style: italic; font-weight: 600;
    line-height: 37px; color: var(--quote-ink); letter-spacing: -0.4px;
  }
</style>
</head>
<body>
  <section class="card card-front" aria-label="Business card front">
    <h1 class="person-name">Dana Mireau</h1>
    <p class="person-title">Chief Performance Strategist</p>
    <div class="divider"></div>
    <h2 class="company-name">Brightlumo Partners, Inc.</h2>
    <p class="address">2180 Lakeview Road<br>Suite 410, Millbrook, MI 48300</p>
    <ul class="contact-list">
      <li>
        <svg viewBox="0 0 20 20" fill="none" stroke="#444" stroke-width="1.2"><circle cx="10" cy="10" r="8.5"/><ellipse cx="10" cy="10" rx="4" ry="8.5"/><line x1="1.5" y1="10" x2="18.5" y2="10"/><line x1="3" y1="5.5" x2="17" y2="5.5"/><line x1="3" y1="14.5" x2="17" y2="14.5"/></svg>
        www.brightlumo.com
      </li>
      <li>
        <svg viewBox="0 0 20 16"><rect x="1" y="2" width="18" height="12" fill="#444"/><path d="M1 2 L10 9 L19 2" fill="none" stroke="#fff" stroke-width="1.2"/></svg>
        danam@brightlumo.com
      </li>
      <li>
        <svg viewBox="0 0 20 16" fill="#444"><path d="M2 6 Q10 0 18 6 L16 8 L13 6 L7 6 L4 8 Z"/><rect x="4" y="8" width="12" height="7" rx="1.5"/><circle cx="10" cy="11.5" r="2" fill="#fff"/></svg>
        555 - 618 - 0142
      </li>
      <li>
        <svg viewBox="0 0 20 18" fill="#444"><rect x="6" y="1" width="8" height="16" rx="1.5"/><rect x="7.5" y="3" width="5" height="5" fill="#fff"/><rect x="7.5" y="10" width="5" height="5" fill="#fff" opacity="0.6"/></svg>
        555 - 765 - 0187
      </li>
    </ul>
    <div class="brand-mark">
      <span class="brand-dot"></span>
      <span class="brand-name">brightlumo</span>
    </div>
  </section>

  <section class="card card-back" aria-label="Business card back">
    <div class="fire-field" role="img" aria-label="Photograph of billowing orange and yellow fire filling the card"></div>
    <p class="mission">I equip results-oriented<br>business leaders to turn<br>their people problems into<br>profits in six months or less.</p>
  </section>
</body>
</html>
```